Website Redesign - Money is Guaranteed!

I would like a site similar to this: http://www.givewheelsforheroes.example

old site: http://www.autosforpatriots.example

Create a professional website; a car donation site seeking leads to return calls.

Please see http://www.givewheelsforheroes.example for the concept I am after.

The webpage should have a professional feel. The pages to include are 'Home', 'About us' and 'Get Started'

Industry/Entity Type

It Professional

Coding

Coded - Design and coding required

Number of Pages Required

1 page

```html
<!DOCTYPE html>
<html lang="en">
<head>
<meta charset="utf-8">
<title>Autos for Patriots – Donate Your Car</title>
<link rel="stylesheet" href="https://fonts.googleapis.com/css2?family=Raleway:wght@500;600;700&family=Open+Sans:ital,wght@0,400;0,600;0,700;1,400&display=swap">
<style>
:root{
  --navy:#0f2e6e;
  --navy-deep:#0b2560;
  --blue:#2f5aa8;
  --blue-top:#1c4fa0;
  --red:#c0161b;
  --red-dark:#a90f14;
  --ink:#333;
  --muted:#555;
  --panel:#f3f3f3;
  --line:#e2e2e2;
  --white:#fff;
}
*{box-sizing:border-box;margin:0;padding:0}
html,body{width:1200px;height:2866px;overflow:hidden}
body{font-family:"Open Sans",Arial,sans-serif;color:var(--ink);background:var(--white);position:relative;font-size:11px;line-height:1.65}
h1,h2,h3,h4{font-family:"Raleway",Arial,sans-serif}
.abs{position:absolute}

/* header */
.topbar{left:0;top:0;width:1200px;height:80px;background:linear-gradient(180deg,#2a62b8,var(--blue-top))}
.navbar{left:0;top:80px;width:1200px;height:54px;background:var(--navy)}
.brand{left:160px;top:22px;display:flex;align-items:center;gap:10px;color:var(--white);font-family:"Raleway",sans-serif;font-weight:700;font-size:22px}
.brand-dot{width:26px;height:26px;border-radius:50%;background:var(--red)}
.nav{left:160px;top:80px;height:54px;display:flex;align-items:center;gap:48px}
.nav a{color:var(--white);text-decoration:none;font-family:"Raleway",sans-serif;font-weight:700;font-size:14px}

/* hero */
.hero{left:0;top:134px;width:1200px;height:386px;background:linear-gradient(100deg,#c9ccd0 0%,#eceeef 30%,#e3e4e4 60%,#d5d6d6 100%)}
.hero-title{left:160px;top:40px;width:420px;text-align:center;color:var(--red);font-family:"Raleway",sans-serif;font-weight:700;font-size:25px;line-height:1.3}
.hero-car{left:0;top:90px;width:320px;height:296px;background:linear-gradient(160deg,#c7c9cc,#8d9095);border-radius:0 120px 0 0}
.hero-people{left:380px;top:90px;width:340px;height:296px;background:linear-gradient(180deg,#b7b5ae,#8c8676)}

/* donation form */
.donate-panel{left:720px;top:0;width:318px;height:520px;background:var(--red);padding:12px 18px;color:var(--white)}
.donate-panel .pitch{text-align:center;font-family:"Raleway",sans-serif;font-weight:700;font-size:17px}
.donate-panel .phone{text-align:center;font-family:"Raleway",sans-serif;font-weight:700;font-size:27px;margin-top:2px}
.donate-panel .note{text-align:center;font-style:italic;font-size:11px;margin-top:22px;margin-bottom:16px}
.field-row{display:flex;gap:6px;margin-bottom:8px}
.field{flex:1;height:34px;background:var(--white);border-radius:2px;color:#999;font-style:italic;font-size:10px;padding:9px 10px;position:relative}
.field.select::after{content:"";position:absolute;right:10px;top:15px;border:4px solid transparent;border-top-color:#666}
.donate-panel h3{font-size:18px;font-weight:700;margin:10px 0 10px}
.btn-donate{height:42px;background:#141414;color:var(--white);font-weight:700;font-size:12px;display:flex;align-items:center;justify-content:center;gap:6px;margin-top:6px}

/* section headers */
.accent{height:5px;width:294px;background:var(--navy)}
.accent.red{background:var(--red)}
.section-title{font-size:27px;font-weight:600;color:var(--navy)}
.section-title.light{color:var(--white)}

/* how it works */
.steps{left:160px;top:634px;width:878px;display:flex;gap:30px}
.step{flex:1;display:flex;gap:14px}
.step svg{flex:none}
.step h4{color:var(--red);font-family:"Open Sans",sans-serif;font-weight:600;font-size:13px;margin-bottom:6px}
.step p{font-size:10px;color:var(--muted)}

/* charities */
.charities{left:0;top:793px;width:1200px;height:482px;background:var(--blue)}
.why-card{left:162px;top:888px;width:876px;height:325px;background:var(--white);box-shadow:0 2px 8px rgba(0,0,0,.25);overflow:hidden}
.why-text{left:32px;top:42px;width:390px}
.why-text h3{color:var(--red);font-weight:700;font-size:19px;margin-bottom:18px}
.why-text p{font-size:10px;color:#222;margin-bottom:14px;line-height:1.6}
.why-photo{left:360px;top:0;width:516px;height:325px;background:linear-gradient(90deg,rgba(255,255,255,1) 0%,rgba(190,205,220,.6) 22%,#a9bfd6 45%,#8aa3bd 70%,#7b8a8e 100%)}

/* tax */
.tax-title{left:0;top:1318px;width:1200px;text-align:center;font-size:27px;font-weight:600;color:var(--navy)}
.tax-intro{left:360px;top:1370px;width:480px;text-align:center;font-size:10px;color:var(--muted)}
.tax-box{top:1447px;width:422px;height:216px;background:var(--panel);border:1px solid var(--line);padding:28px 32px}
.tax-box h3{color:var(--red);font-size:19px;font-weight:700;line-height:1.4;margin-bottom:14px}
.tax-box p{font-size:10px;color:var(--muted)}
.file-title{left:162px;top:1698px;color:var(--red);font-size:19px;font-weight:700}
.file-text{left:162px;top:1738px;width:876px;font-size:10px;color:var(--muted);line-height:1.75}
.keys{left:0;top:1790px;width:140px;height:92px;background:linear-gradient(160deg,#d7d9db,#6d7176);border-radius:0 70px 0 0}

/* donate today */
.today{left:0;top:1882px;width:1200px;height:511px;background:linear-gradient(180deg,var(--navy-deep),#12357d)}
.today-title{left:160px;top:88px;font-size:27px;font-weight:600;color:var(--white)}
.today-intro{left:160px;top:140px;width:440px;font-size:10px;color:#dbe3f2}
.benefits{left:160px;top:230px;list-style:none}
.benefits li{display:flex;align-items:center;gap:18px;color:var(--white);font-size:16px;height:41px}
.red-car{left:630px;top:144px;width:480px;height:248px;background:linear-gradient(180deg,#e0272d,#a5161a);border-radius:120px 140px 40px 40px}

/* program */
.program-title{left:160px;top:2422px;font-size:27px;font-weight:600;color:var(--navy)}
.programs{left:160px;top:2520px;width:922px;display:flex}
.program{flex:1;text-align:center}
.program .icon{height:64px;display:flex;justify-content:center;align-items:flex-end}
.program h4{font-family:"Open Sans",sans-serif;color:var(--red);font-weight:600;font-size:13px;line-height:1.5;margin:22px 0 18px}
.program p{font-size:10px;color:var(--muted);width:176px;margin:0 auto}

/* footer */
.footer-rule{left:0;top:2786px;width:1200px;height:4px;background:var(--red)}
.badges{left:160px;top:2808px;display:flex;align-items:center;gap:14px}
.badge-seal{width:46px;height:46px;border-radius:50%;background:#c9d3e2}
.badge-secure{width:92px;height:34px;background:#dcdcdc;border-radius:2px}
.divider{width:1px;height:40px;background:#ccc}
.social{display:flex;gap:6px}
.social span{width:30px;height:30px;border-radius:50%;display:block}
.footer-legal{left:782px;top:2808px;font-size:10px;color:#333;line-height:2}
.footer-legal a{color:#333;text-decoration:none;margin-right:12px}
.footer-code{left:1068px;top:2815px;font-size:10px;color:#555}
</style>
</head>
<body>

<header>
  <div class="abs topbar"></div>
  <div class="abs navbar"></div>
  <div class="abs brand"><span class="brand-dot"></span>Autos for Patriots</div>
  <nav class="abs nav">
    <a href="#how">HOW IT WORKS</a>
    <a href="#charities">CHARITIES</a>
    <a href="#tax">TAX DEDUCTION</a>
    <a href="#faq">FAQ</a>
  </nav>
</header>

<section class="abs hero">
  <div class="abs hero-car" role="img" aria-label="Silver sedan parked at left"></div>
  <div class="abs hero-people" role="img" aria-label="Soldier in uniform welcoming a running child"></div>
  <h1 class="abs hero-title">Donate Your Car: Full Tax Deduction - Running or Not</h1>
</section>

<aside class="abs donate-panel">
  <div class="pitch">Donate Car to Charity!</div>
  <div class="phone">1-800-555-0142</div>
  <div class="note">Or Fill out the form below to instantly donate online</div>
  <div class="field-row"><div class="field">First Name:</div><div class="field">Last Name:</div></div>
  <div class="field-row"><div class="field">Phone:</div></div>
  <div class="field-row"><div class="field">Email:</div></div>
  <div class="field-row"><div class="field">Address:</div><div class="field">Zip Code:</div></div>
  <h3>Vehicle Donation Information</h3>
  <div class="field-row"><div class="field select">Year of Vehicle:</div></div>
  <div class="field-row"><div class="field select">Make of Vehicle:</div><div class="field select">Model of Vehicle:</div></div>
  <div class="btn-donate">CLICK HERE TO DONATE NOW
    <svg width="12" height="12" viewBox="0 0 12 12"><circle cx="6" cy="6" r="6" fill="#fff"/><path d="M5 3l3 3-3 3" stroke="#141414" stroke-width="1.6" fill="none"/></svg>
  </div>
</aside>

<section id="how">
  <div class="abs accent" style="left:160px;top:520px"></div>
  <h2 class="abs section-title" style="left:160px;top:544px">How It Works</h2>
  <div class="abs steps">
    <div class="step">
      <svg width="44" height="64" viewBox="0 0 44 64"><rect x="2" y="4" width="38" height="48" fill="var(--navy)"/><g stroke="#fff" stroke-width="2.4"><line x1="9" y1="16" x2="33" y2="16"/><line x1="9" y1="24" x2="33" y2="24"/><line x1="9" y1="32" x2="33" y2="32"/><line x1="9" y1="40" x2="26" y2="40"/></g><path d="M30 46l6 14 2-6 6-2z" fill="var(--navy)"/></svg>
      <div><h4>1. Fill out the simple form</h4><p>Sed ut perspiciatis unde omnisuptatem accusantium dolorue laudantiutem accu santmsantium dolorue laudota.</p></div>
    </div>
    <div class="step">
      <svg width="44" height="64" viewBox="0 0 44 64"><path d="M22 2v14a6 6 0 1 1-6 6" stroke="var(--navy)" stroke-width="3" fill="none"/><path d="M6 48l4-10h24l4 10v10H6z" fill="var(--navy)"/><circle cx="13" cy="52" r="3" fill="#fff"/><circle cx="31" cy="52" r="3" fill="#fff"/></svg>
      <div><h4>2. Schedule your free pick-up</h4><p>Sed ut perspiciatis unde omnisuptatem accusantium dolorue laudantiutem accu santmsantium dolorue laudota.</p></div>
    </div>
    <div class="step">
      <svg width="44" height="64" viewBox="0 0 44 64"><rect x="2" y="4" width="40" height="56" fill="var(--navy)"/><rect x="8" y="10" width="28" height="12" fill="#fff"/><path d="M6 30l16 14 16-14" stroke="#fff" stroke-width="2.4" fill="none"/></svg>
      <div><h4>3. Receive tax deduction</h4><p>Sed ut perspiciatis unde omnisuptatem accusantium dolorue laudantiutem accu santmsantium dolorue laudota.</p></div>
    </div>
  </div>
</section>

<section id="charities">
  <div class="abs charities"></div>
  <div class="abs accent red" style="left:160px;top:793px"></div>
  <h2 class="abs section-title light" style="left:160px;top:816px">Charities We Work With</h2>
  <div class="abs why-card">
    <div class="abs why-photo" role="img" aria-label="Veteran in a wheelchair on a lakeside pier with arms outstretched"></div>
    <div class="abs why-text">
      <h3>Why Donate Your Car to Us?</h3>
      <p>&nbsp;IRS 501(c)3 Approved: Free 24/7 Pickup with No DMV Hassles.</p>
      <p>Free Local Towing to You: We will pick up your car donation, running or not, when it's most convenient, at home or work.</p>
      <p>All Cars Accepted: We take your car regardless of its condition or registration status.</p>
      <p>Income Tax Deduction: We issue you an IRS tax receipt &amp; offer the largest resale network to get you the highest tax write-off possible.</p>
    </div>
  </div>
</section>

<section id="tax">
  <div class="abs accent red" style="left:453px;top:1275px"></div>
  <h2 class="abs tax-title">Tax Deduction Information For Your Car Donation</h2>
  <p class="abs tax-intro">Sed ut perspiciatis unde omnis iste natus error sit voluptatem accusantium doloremque ud antium, totam rem aperiam, eaque ipsa quae ab illo inventore veritatis et qua.</p>
  <div class="abs tax-box" style="left:162px">
    <h3>If Your Car Donation Sells for<br>$500 Or Less</h3>
    <p>Sed ut perspiciatis unde omnis iste natus error sit voluptatem accusn tium doloremque ud antium, totam rem aperiam, eaque ipsa quae illo inventore veritatis et quasi architectoea tae vitae dicta sunt explicamo enim ipsam voluptatem quia voluptas sit aspernat</p>
  </div>
  <div class="abs tax-box" style="left:616px">
    <h3>If Your Car Donation Sells for<br>$501 Or More</h3>
    <p>Sed ut perspiciatis unde omnis iste natus error sit voluptatem accusn tium doloremque ud antium, totam rem aperiam, eaque ipsa quae illo inventore veritatis et quasi architectoea tae vitae dicta sunt explicamo enim ipsam voluptatem quia voluptas sit aspernat</p>
  </div>
  <h3 class="abs file-title">How to file your taxes</h3>
  <p class="abs file-text">Sed ut perspiciatis unde omnis iste natus error sit voluptatem accusantium doloremque ud antium, totam rem aperiam, eaque ipsa quae ab illo inventore veritatis et si architectoea tae vitae dicta sunt explicabomo enim ipsam voluptatem quia voluptas sit aspernated ut perspiciatis unde omnis iste natus error sit voluptatem accusantium doloremque ud antium, totam rem aperiam, eaque ipsa quae ab illo inventore veritatis et quasi architectoea tae vitae dicta sunt explicabomo enim ipsam voluptatem uia voluptas sit aspve ab illo inventore veritatis et quasi architecternat.</p>
  <div class="abs keys" role="img" aria-label="Car keys resting at the page edge"></div>
</section>

<section id="faq">
  <div class="abs today"></div>
  <div class="abs accent red" style="left:160px;top:1882px"></div>
  <h2 class="abs today-title" style="top:1970px">Donate Your Car Today!</h2>
  <p class="abs today-intro" style="top:2022px">Sed ut perspiciatis unde omnis iste natus error sit voluptatem accusantium dolore mque laudantium, totam rem aperiam, eaque ipsa quae ab illo inventore veritatis et quasi architecto beatae vitae dicta sunt explicaboqui dolorem ipsum quia.</p>
  <ul class="abs benefits" style="top:2112px">
    <li><svg width="12" height="12" viewBox="0 0 12 12"><circle cx="6" cy="6" r="6" fill="#fff"/><path d="M5 3l3 3-3 3" stroke="var(--navy)" stroke-width="1.6" fill="none"/></svg>You have no costs.</li>
    <li><svg width="12" height="12" viewBox="0 0 12 12"><circle cx="6" cy="6" r="6" fill="#fff"/><path d="M5 3l3 3-3 3" stroke="var(--navy)" stroke-width="1.6" fill="none"/></svg>Free towing, running or not.</li>
    <li><svg width="12" height="12" viewBox="0 0 12 12"><circle cx="6" cy="6" r="6" fill="#fff"/><path d="M5 3l3 3-3 3" stroke="var(--navy)" stroke-width="1.6" fill="none"/></svg>We issue you an IRS tax receipt.</li>
    <li><svg width="12" height="12" viewBox="0 0 12 12"><circle cx="6" cy="6" r="6" fill="#fff"/><path d="M5 3l3 3-3 3" stroke="var(--navy)" stroke-width="1.6" fill="none"/></svg>We take care of all paperwork.</li>
    <li><svg width="12" height="12" viewBox="0 0 12 12"><circle cx="6" cy="6" r="6" fill="#fff"/><path d="M5 3l3 3-3 3" stroke="var(--navy)" stroke-width="1.6" fill="none"/></svg>And we take care of DMV &amp; Smog issues.</li>
  </ul>
  <div class="abs red-car" style="top:2026px" role="img" aria-label="Red sedan, front three-quarter view"></div>
</section>

<section>
  <div class="abs accent red" style="left:160px;top:2393px"></div>
  <h2 class="abs program-title">Car Donation Program</h2>
  <div class="abs programs">
    <div class="program">
      <div class="icon"><svg width="44" height="56" viewBox="0 0 44 56"><path d="M22 2a18 18 0 0 1 18 18c0 14-18 34-18 34S4 34 4 20A18 18 0 0 1 22 2z" fill="var(--navy)"/><circle cx="22" cy="20" r="7" fill="#fff"/></svg></div>
      <h4>Donations<br>Accepted Nationwide</h4>
      <p>Sed ut perspiciatis unde omnis sit voluptatem accusantium dolorue laudantiutem accusantmota.</p>
    </div>
    <div class="program">
      <div class="icon"><svg width="64" height="56" viewBox="0 0 64 56"><path d="M12 24l6-16h28l6 16" stroke="var(--navy)" stroke-width="5" fill="none"/><rect x="4" y="24" width="56" height="20" rx="4" fill="var(--navy)"/><circle cx="16" cy="34" r="4" fill="#fff"/><circle cx="48" cy="34" r="4" fill="#fff"/><rect x="8" y="44" width="10" height="10" fill="var(--navy)"/><rect x="46" y="44" width="10" height="10" fill="var(--navy)"/></svg></div>
      <h4>All Vehicle<br>Types Welcome</h4>
      <p>Sed ut perspiciatis unde omnis sit voluptatem accusantium dolorue laudantiutem accusantmota.</p>
    </div>
    <div class="program">
      <div class="icon"><svg width="44" height="56" viewBox="0 0 44 56"><path d="M4 2h36v52l-6-4-6 4-6-4-6 4-6-4-6 4z" fill="var(--navy)"/><g stroke="#fff" stroke-width="3"><line x1="11" y1="14" x2="33" y2="14"/><line x1="11" y1="23" x2="33" y2="23"/><line x1="11" y1="32" x2="26" y2="32"/></g></svg></div>
      <h4>Tax Deductible</h4>
      <p>Sed ut perspiciatis unde omnis sit voluptatem accusantium dolorue laudantiutem accusantmota.</p>
    </div>
    <div class="program">
      <div class="icon"><svg width="70" height="56" viewBox="0 0 70 56"><path d="M4 42V26h14l8-12h14v28z" fill="var(--navy)"/><rect x="40" y="30" width="26" height="12" fill="var(--navy)"/><path d="M44 30L60 8" stroke="var(--navy)" stroke-width="4"/><circle cx="16" cy="46" r="7" fill="var(--navy)"/><circle cx="16" cy="46" r="3" fill="#fff"/><circle cx="52" cy="46" r="7" fill="var(--navy)"/><circle cx="52" cy="46" r="3" fill="#fff"/><rect x="28" y="18" width="8" height="8" fill="#fff"/></svg></div>
      <h4>Towing is Free</h4>
      <p>Sed ut perspiciatis unde omnis sit voluptatem accusantium dolorue laudantiutem accusantmota.</p>
    </div>
  </div>
</section>

<footer>
  <div class="abs footer-rule"></div>
  <div class="abs badges">
    <span class="badge-seal" role="img" aria-label="Trust seal"></span>
    <span class="badge-secure" role="img" aria-label="Security certificate badge"></span>
    <span class="divider"></span>
    <div class="social">
      <span style="background:#4aa3df" role="img" aria-label="Social link"></span>
      <span style="background:#3b5b9c" role="img" aria-label="Social link"></span>
      <span style="background:#1f6fa3" role="img" aria-label="Social link"></span>
      <span style="background:#d24a3b" role="img" aria-label="Social link"></span>
    </div>
  </div>
  <div class="abs footer-legal">
    © 2017 autosforpatriots. All Copyrights are Reserved.<br>
    <a href="#">Terms of Use</a><a href="#">Privacy Policy</a><a href="#">Sitemap</a>
  </div>
  <div class="abs footer-code">C4</div>
</footer>

</body>
</html>
```